CalmHaven Webpage for Integrative and Holistic Psychiatric Practice

We need a webpage designed for a medical practice that focuses on integrative and holistic psychiatry. We focus on providing care to mothers and families. The name of the company is Calm Haven, incorporated, A Professional Medical Corporation.

We'd like the color palette to be earthy/natural with the same look and feel as our logo that's attached. We're not set on anything, so feel free to have fun with the palette. We just want it to be warm and inviting in particular for Moms!

We'd like to have our logo in the top left with links below it either centered or to the right. We really like websites like http://www.brightmeadowclinic.example/home.html and http://www.tarnwickmindpartners.example/site/ to give you an idea of what we're looking for.

For links, we're looking for the following. Dummy text is fine, we're still getting content together:

* Home
* About Us - this page would have headings for Directions, Staff, Appointment Scheduling
* Services Provided - headings for 8 different services
* Patient Resources - headings for Patient Forms, Fees, Articles
* FAQ
* Contact Us

The webpage will be hosted as an Office 365 Public Website, so feel free to use whatever SharePoint integration you would like, but it's not necessary.

Thank you!

```html
<!DOCTYPE html>
<html lang="en">
<head>
<meta charset="utf-8">
<title>Calm Haven – Integrative &amp; Holistic Psychiatry</title>
<link rel="stylesheet" href="https://fonts.googleapis.com/css2?family=Lato:ital,wght@0,400;0,700;0,900;1,400;1,700;1,900&family=Oswald:wght@400&display=swap">
<style>
:root{
  --brown:#5c2a06;
  --green:#3a7a10;
  --green-dark:#2c5f0a;
  --hero-text:#2f7d0c;
  --text:#3b3b3b;
  --muted:#555;
  --rule:#d9d9d9;
  --band:#efefef;
  --white:#fff;
  --accent-gold:#8a4a12;
  --footer-rule:#74401a;
}
*{box-sizing:border-box;margin:0;padding:0}
html,body{width:853px;height:1200px;overflow:hidden}
body{position:relative;background:var(--white);font-family:"Lato",Arial,sans-serif;color:var(--text)}
.abs{position:absolute}

/* header */
.site-header{left:0;top:0;width:853px;height:78px;background:linear-gradient(#fff,#f7f4f1);border-top:2px solid var(--brown)}
.brand{left:95px;top:22px;display:flex;align-items:center;gap:8px;font-size:22px;font-weight:700;color:var(--green-dark)}
.brand-mark{width:26px;height:26px;border-radius:50%;background:var(--green)}
.call{right:93px;top:30px;display:flex;align-items:center;gap:6px;font-size:15px;color:var(--text)}
.call em{font-style:normal;color:var(--green)}
.call .ico{width:19px;height:19px;border-radius:50%;background:var(--green-dark);display:flex;align-items:center;justify-content:center}

/* nav */
.main-nav{left:0;top:78px;width:853px;height:34px;background:var(--brown)}
.main-nav ul{list-style:none;position:absolute;left:93px;top:0;display:flex;height:34px}
.main-nav li{height:34px;display:flex;align-items:center;justify-content:center;color:#fff;font-size:11px;font-weight:700;border-right:1px solid #7a4316}
.main-nav li.active{background:var(--green)}

/* hero */
.hero{left:0;top:112px;width:853px;height:320px;background:linear-gradient(100deg,#6f8f3a 0%,#a9c36b 35%,#8fb54e 55%,#c9d9b6 80%,#e6ede1 100%)}
.hero-title{left:95px;top:198px;font-size:22px;line-height:30px;font-weight:900;font-style:italic;color:var(--hero-text);text-shadow:0 0 2px #fff,0 0 3px #fff,0 1px 4px rgba(255,255,255,.9)}
.hero-curve{left:0;top:370px}
.dots{left:381px;top:354px;width:91px;height:24px;background:var(--brown);border-radius:6px 6px 0 0;display:flex;gap:6px;align-items:center;justify-content:center}
.dots span{width:10px;height:10px;border-radius:50%;background:#ddd}
.dots span.on{background:var(--green);border:2px solid #ddd}

/* features */
.features{left:93px;top:376px;width:667px;height:190px;background:#fff;border-top:4px solid var(--brown);box-shadow:0 6px 10px rgba(0,0,0,.04);display:flex}
.feature{width:222px;text-align:center;position:relative;padding-top:62px}
.ribbon{position:absolute;top:0;left:50%;transform:translateX(-50%)}
.feature h3{font-size:17px;font-weight:400;color:#333;margin-bottom:8px}
.feature p{font-size:9.5px;line-height:14px;color:var(--muted);padding:0 12px}
.btn{display:inline-block;background:var(--green-dark);color:#fff;font-size:10px;font-weight:700;padding:5px 7px;border-radius:2px;border:1px solid #1f4a06}
.feature .btn{margin-top:12px}

/* welcome */
.welcome-head{left:100px;top:590px;width:420px;display:flex;align-items:center;gap:8px}
.welcome-head .dot{width:22px;height:22px;border-radius:50%;background:var(--green)}
.welcome-head h2{font-size:17px;font-style:italic;font-weight:400;color:var(--brown)}
.welcome-head h2 b{color:var(--green);font-weight:400}
.welcome-head .line{flex:1;height:1px;background:#ccc;margin-top:8px}
.welcome-text{left:101px;top:627px;width:422px;font-size:9.4px;line-height:14.7px;color:#444}
.welcome-btn{left:100px;top:725px}
.video{left:559px;top:587px;width:194px;height:146px;border:1px solid #ccc;padding:3px;background:#fff}
.video-frame{width:186px;height:116px;background:linear-gradient(135deg,#5e7a4a,#9cab80 50%,#c9b8a1)}
.video-bar{width:186px;height:22px;background:#111;display:flex;align-items:center;gap:6px;padding:0 6px;color:#fff;font-size:8px;font-weight:700}
.video-bar .track{flex:1;height:5px;background:#444;border-radius:3px;position:relative}
.video-bar .track i{position:absolute;left:24px;top:-2px;width:9px;height:9px;border-radius:50%;background:#aaa}

/* band */
.band{left:0;top:767px;width:853px;height:200px;background:var(--band)}
.section-title{font-size:20px;font-weight:400;color:#333}
.section-title b{color:var(--green);font-weight:400}
.news{left:101px;top:782px;width:304px}
.testimonials{left:449px;top:782px;width:304px}
.head-row{display:flex;justify-content:space-between;align-items:center;border-bottom:1px solid var(--rule);padding-bottom:3px}
.arrows{display:flex;gap:3px}
.arrows span{width:13px;height:13px;border:1px solid #999;border-radius:50%;font-size:8px;line-height:11px;text-align:center;color:#666}
.news-item{display:flex;gap:11px;padding:11px 0 13px;border-bottom:1px solid var(--rule)}
.news-item:last-child{border-bottom:none}
.date{width:35px;flex:none;text-align:center}
.date .d{background:var(--green-dark);color:#fff;font-family:"Oswald",sans-serif;font-size:17px;height:27px;line-height:27px}
.date .m{background:var(--brown);color:#fff;font-size:8.5px;height:13px;line-height:13px}
.news-item h4{font-size:9.6px;font-weight:700;color:#222;margin-bottom:2px}
.news-item p{font-size:9.4px;line-height:14.5px;color:#444}
.divider{left:425px;top:778px;width:1px;height:160px;background:#ddd}
.portrait{left:447px;top:822px;width:74px;height:74px;border-radius:50%;border:3px solid #fff;box-shadow:0 0 0 1px #ccc;background:radial-gradient(circle at 50% 40%,#d9ae8b,#8a5a32)}
.quote{left:545px;top:825px;width:208px;font-size:9.6px;line-height:18px;font-style:italic;color:#444}
.quote .q{font-size:22px;color:#bbb;font-weight:900;line-height:0;vertical-align:-6px}
.author{left:545px;top:905px;font-size:11px;font-weight:700;color:var(--accent-gold)}

/* footer */
.footer-wave{left:0;top:925px}
.footer{left:0;top:1005px;width:853px;height:195px;background:var(--brown)}
.fcol{position:absolute;top:10px}
.fcol h5{font-size:12px;font-weight:700;color:#fff;padding-bottom:5px;border-bottom:1px solid var(--footer-rule);margin-bottom:3px}
.links{list-style:none;font-size:9.5px;color:#fff;line-height:18.6px}
.fcol p{font-size:8.6px;line-height:12px;color:#fff;margin-top:4px}
.email{margin-top:10px;width:148px;height:19px;background:#fff;border-radius:2px;font-size:8.5px;font-style:italic;color:#666;padding:4px 10px}
.sub{margin-top:12px;width:82px;height:21px;background:var(--green-dark);border:1px solid #a9c98d;border-radius:3px;color:#fff;font-size:10.5px;font-weight:700;text-align:center;line-height:19px}
.crow{display:flex;gap:10px;font-size:9px;line-height:15px;color:#fff;margin-bottom:13px}
.crow:first-of-type{margin-top:6px}
.crow svg{flex:none;margin-top:2px}
.crow.big{font-size:10px}
.map{width:160px;height:87px;margin-top:10px;border:2px solid #fff;background:linear-gradient(135deg,#c7d8e6,#e8e2cf 50%,#d4e3c4)}
.footer-rule{left:93px;top:1158px;width:667px;height:1px;background:var(--footer-rule)}
.copy{left:95px;top:1172px;font-size:9px;color:#fff}
.social{left:696px;top:1170px;display:flex;gap:6px}
.social span{width:16px;height:16px;background:#fff;border-radius:2px}
</style>
</head>
<body>

<header class="site-header abs">
  <div class="brand abs"><span class="brand-mark"></span>Calm Haven</div>
  <div class="call abs">
    <span class="ico"><svg width="11" height="11" viewBox="0 0 24 24"><path fill="#fff" d="M6.6 10.8a15 15 0 006.6 6.6l2.2-2.2c.3-.3.7-.4 1-.2 1.1.4 2.3.6 3.6.6.6 0 1 .4 1 1V20c0 .6-.4 1-1 1A17 17 0 013 4c0-.6.4-1 1-1h3.5c.6 0 1 .4 1 1 0 1.3.2 2.5.6 3.6.1.3 0 .7-.2 1z"/></svg></span>
    <em>Call Now!</em> (555) 318-2047
  </div>
</header>

<nav class="main-nav abs">
  <ul>
    <li class="active" style="width:94px">HOME</li>
    <li style="width:116px">ABOUT US</li>
    <li style="width:112px">SERVICES</li>
    <li style="width:86px">FAQ</li>
    <li style="width:166px">PATIENT RESOURCES</li>
    <li style="width:126px;border-right:none">CONTACT US</li>
  </ul>
</nav>

<section class="hero abs" role="img" aria-label="Photo of a smiling older couple walking outdoors among green trees"></section>
<div class="hero-title abs">Lorem ipsum dolor sit amet<br>consectetuer adipiscing elit<br>sed diam nonummy nibh</div>
<svg class="hero-curve abs" width="853" height="70" viewBox="0 0 853 70">
  <path d="M0 40 C40 45 80 55 93 58 L760 58 C790 50 820 40 853 34 L853 70 L0 70Z" fill="#fdf6f1"/>
  <path d="M0 40 C40 45 80 55 93 58 M760 58 C790 50 820 40 853 34" stroke="#5c2a06" stroke-width="2.5" fill="none"/>
</svg>
<div class="dots abs"><span class="on"></span><span></span><span></span><span></span></div>

<section class="features abs">
  <div class="feature">
    <svg class="ribbon" width="43" height="60" viewBox="0 0 43 60"><path d="M0 0H43V54L21.5 60 0 54Z" fill="#3a7a10"/><path d="M0 54L21.5 60 43 54" stroke="#5c2a06" stroke-width="2" fill="none"/><circle cx="18" cy="28" r="7" fill="none" stroke="#fff" stroke-width="3.5"/><circle cx="29" cy="20" r="4" fill="none" stroke="#fff" stroke-width="2.5"/></svg>
    <h3>We Services Provided</h3>
    <p>It is a long established fact that a rea distracted by the readable content of a page when looking at its layout.</p>
    <span class="btn">Read More</span>
  </div>
  <div class="feature">
    <svg class="ribbon" width="43" height="60" viewBox="0 0 43 60"><path d="M0 0H43V54L21.5 60 0 54Z" fill="#3a7a10"/><path d="M0 54L21.5 60 43 54" stroke="#5c2a06" stroke-width="2" fill="none"/><rect x="10" y="13" width="23" height="21" rx="2" fill="#fff"/><rect x="10" y="13" width="23" height="5" fill="#dfe9d6"/><g fill="#3a7a10"><rect x="13" y="21" width="3" height="3"/><rect x="18" y="21" width="3" height="3"/><rect x="23" y="21" width="3" height="3"/><rect x="28" y="21" width="3" height="3"/><rect x="13" y="27" width="3" height="3"/><rect x="18" y="27" width="3" height="3"/><rect x="23" y="27" width="3" height="3"/></g></svg>
    <h3>Appointment Scheduling</h3>
    <p>It is a long established fact that a rea distracted by the readable content of a page when looking at its layout.</p>
    <span class="btn">Read More</span>
  </div>
  <div class="feature">
    <svg class="ribbon" width="43" height="60" viewBox="0 0 43 60"><path d="M0 0H43V54L21.5 60 0 54Z" fill="#3a7a10"/><path d="M0 54L21.5 60 43 54" stroke="#5c2a06" stroke-width="2" fill="none"/><g fill="#fff"><circle cx="21.5" cy="18" r="4.5"/><path d="M14 34c0-6 3-9 7.5-9s7.5 3 7.5 9z"/><circle cx="12" cy="21" r="3.3"/><path d="M6 33c0-4 2-7 6-7 1 0 2 .3 2.5.7-1.5 1.8-2 3.8-2 6.3z"/><circle cx="31" cy="21" r="3.3"/><path d="M37 33c0-4-2-7-6-7-1 0-2 .3-2.5.7 1.5 1.8 2 3.8 2 6.3z"/></g></svg>
    <h3>Patient Resources</h3>
    <p>It is a long established fact that a rea distracted by the readable content of a page when looking at its layout.</p>
    <span class="btn">Read More</span>
  </div>
</section>

<div class="welcome-head abs"><span class="dot"></span><h2>Welcome <b>Calm Haven</b></h2><span class="line"></span></div>
<p class="welcome-text abs">Lorem ipsum dolor sit amet, consectetuer adipiscing elit, sed diam nonummy nibh euismod tincidunt ut laoreet dolore magna aliquam erat volutpat. Ut wisi enim ad minim veniam, quis nostrud exerci tation ullamcorper suscipit lobortis nisl ut aliquip ex ea commodo consequat. Duis autem vel eum iriure dolor in hendrerit in vulputate velit esse molestie consequat, vel illum dolore eu feugiat nulla facilisis at vero eros et accumsan et iusto odio dignissim qui blandit praesent luptatum zzril delenit augue duis dolore te feugait nulla facilisi.</p>
<span class="btn welcome-btn abs">Read More</span>

<div class="video abs">
  <div class="video-frame" role="img" aria-label="Video still of a happy young couple outdoors"></div>
  <div class="video-bar">
    <svg width="8" height="9" viewBox="0 0 8 9"><path d="M0 0L8 4.5 0 9Z" fill="#fff"/></svg>
    <span>04:59</span><span class="track"><i></i></span><span>10:35</span>
    <svg width="10" height="9" viewBox="0 0 10 9"><path d="M0 3H2.5L6 0V9L2.5 6H0Z" fill="#fff"/><path d="M7.5 2.5Q9 4.5 7.5 6.5" stroke="#fff" fill="none"/></svg>
  </div>
</div>

<section class="band abs"></section>
<div class="news abs">
  <div class="head-row"><h2 class="section-title">Latest <b>News</b></h2><div class="arrows"><span>‹</span><span>›</span></div></div>
  <div class="news-item">
    <div class="date"><div class="d">04</div><div class="m">OCT</div></div>
    <div><h4>Sed ut perspiciatis unde omnis iste natus error sit</h4><p>voluptatem accusant &nbsp;doloremque laudantium, totamrem okl aperiam, eaque ipsa quae ab illoi</p></div>
  </div>
  <div class="news-item">
    <div class="date"><div class="d">06</div><div class="m">OCT</div></div>
    <div><h4>Sed ut perspiciatis unde omnis iste natus error sit</h4><p>voluptatem accusant &nbsp;doloremque laudantium, totamrem okl aperiam, eaque ipsa quae ab illoi</p></div>
  </div>
</div>
<div class="divider abs"></div>
<div class="testimonials abs">
  <div class="head-row"><h2 class="section-title">Client <b>Testimonials</b></h2><div class="arrows"><span>‹</span><span>›</span></div></div>
</div>
<div class="portrait abs" role="img" aria-label="Portrait photo of a smiling client"></div>
<p class="quote abs"><span class="q">“</span> Lorem ipsum sit amet co adipiscig elitsedudi eiusmod tepor incidiunt ut la dolore maa aliquan ki enim nim veni exercitation ullamco ipsum sdlit amet co adipiscig elitsed do eiusmod tepor <span class="q">”</span></p>
<div class="author abs">- Mara Ellingson</div>

<svg class="footer-wave abs" width="853" height="90" viewBox="0 0 853 90">
  <path d="M0 5 C150 30 350 60 560 45 C680 36 780 25 853 28 L853 90 L0 90Z" fill="#3a7a10"/>
  <path d="M0 30 C180 48 380 64 580 52 C700 44 790 38 853 40" stroke="#fff" stroke-width="3" fill="none"/>
  <path d="M0 33 C180 51 380 67 580 55 C700 47 790 41 853 43 L853 90 L0 90Z" fill="#5c2a06"/>
</svg>
<footer class="footer abs">
  <div class="fcol" style="left:95px;width:96px">
    <h5>Quick Links</h5>
    <ul class="links"><li>HOME</li><li>ABOUT US</li><li>SERVICES</li><li>FAQ</li><li>PATIENT RESOURCES</li><li>CONTACT US</li></ul>
  </div>
  <div class="fcol" style="left:223px;width:150px">
    <h5>Subscribe to Newsletter</h5>
    <p>Get Latest Updates By Entering Your Email Address</p>
    <div class="email">Email Address</div>
    <div class="sub">Subscribe</div>
  </div>
  <div class="fcol" style="left:411px;width:153px">
    <h5>Contact Us</h5>
    <div class="crow"><svg width="9" height="12" viewBox="0 0 9 12"><path d="M4.5 0A4.5 4.5 0 000 4.5C0 8 4.5 12 4.5 12S9 8 9 4.5A4.5 4.5 0 004.5 0Zm0 6.3a1.8 1.8 0 110-3.6 1.8 1.8 0 010 3.6Z" fill="#fff"/></svg><span>Lorem ipsum dolor sit consecte<br>No 5, zip Code: 530916</span></div>
    <div class="crow big"><svg width="11" height="11" viewBox="0 0 24 24"><path fill="#fff" d="M6.6 10.8a15 15 0 006.6 6.6l2.2-2.2c.3-.3.7-.4 1-.2 1.1.4 2.3.6 3.6.6.6 0 1 .4 1 1V20c0 .6-.4 1-1 1A17 17 0 013 4c0-.6.4-1 1-1h3.5c.6 0 1 .4 1 1 0 1.3.2 2.5.6 3.6.1.3 0 .7-.2 1z"/></svg><span>(555) 902-4410</span></div>
    <div class="crow"><svg width="12" height="9" viewBox="0 0 12 9"><rect x=".5" y=".5" width="11" height="8" fill="none" stroke="#fff"/><path d="M.5.5L6 5 11.5.5" stroke="#fff" fill="none"/></svg><span>info@calmhaven.example</span></div>
  </div>
  <div class="fcol" style="left:597px;width:163px">
    <h5>Location Map</h5>
    <div class="map" role="img" aria-label="Street map showing the practice location"></div>
  </div>
</footer>
<div class="footer-rule abs"></div>
<div class="copy abs">© 2014 Calm Haven. All Rights Reserved.</div>
<div class="social abs"><span></span><span></span><span></span></div>

</body>
</html>
```